Gourmet cookie company needs a label designed

We need a label designed for a new cookie company. We make mini cookies. The labels will be placed on either white tins or clear containers. We would like some bright and eye catching label although not child like. Our target customer is adults not kids.
Any color/colors acceptable. The initial label will be a square 4" label but the design should also be able to be formatted to fit on a round label as well in the future.

Text on label: Henrietta's Little Oven Company; Chocolate Chip; All Natural; New Wt. 8.0oz

```html
<!DOCTYPE html>
<html lang="en">
<head>
<meta charset="utf-8">
<title>Henrietta's Little Oven Company – Chocolate Chip Label</title>
<link rel="stylesheet" href="https://fonts.googleapis.com/css2?family=Cabin:wght@400&family=Josefin+Sans:wght@700&display=swap">
<style>
  :root {
    --page-bg: #ffffff;
    --label-white: #ffffff;
    --frame-tan: #d6b68d;
    --text-tan: #d7a886;
    --mint: #e6f2e4;
    --mint-soft: #f1f7ef;
  }
  * { margin: 0; padding: 0; box-sizing: border-box; }
  html, body {
    width: 1200px;
    height: 1200px;
    overflow: hidden;
    background: var(--page-bg);
  }
  .label {
    position: relative;
    width: 1200px;
    height: 1200px;
  }
  .label-shapes {
    position: absolute;
    inset: 0;
    width: 1200px;
    height: 1200px;
  }
  .label-text {
    position: absolute;
    left: 0;
    width: 1200px;
    text-align: center;
    color: var(--text-tan);
    white-space: nowrap;
  }
  .company-name {
    top: 340px;
    font-family: "Cabin", "Gill Sans", sans-serif;
    font-weight: 400;
    font-size: 50px;
    line-height: 84px;
  }
  .flavour {
    top: 548px;
    font-family: "Josefin Sans", "Futura", sans-serif;
    font-weight: 700;
    font-size: 84px;
    line-height: 100px;
    font-variant: small-caps;
    letter-spacing: 2px;
  }
  .product-details {
    top: 730px;
    font-family: "Cabin", "Gill Sans", sans-serif;
    font-weight: 400;
    font-size: 38px;
    line-height: 58px;
  }
</style>
</head>
<body>
  <main class="label">
    <svg class="label-shapes" viewBox="0 0 1200 1200" xmlns="http://www.w3.org/2000/svg" aria-hidden="false">
      <defs>
        <radialGradient id="ornament-tone" cx="600" cy="600" r="585" gradientUnits="userSpaceOnUse">
          <stop offset="0.67" stop-color="var(--mint)"/>
          <stop offset="0.85" stop-color="var(--mint-soft)"/>
          <stop offset="1" stop-color="var(--mint)"/>
        </radialGradient>
      </defs>
      <path class="ornament-band"
            role="img"
            aria-label="Decorative ring of overlapping tan loops with mint fill"
            fill="url(#ornament-tone)"
            fill-rule="evenodd"
            d="M600 30 A570 570 0 1 1 599.9 30 Z M600 206 A394 394 0 1 0 600.1 206 Z"/>
      <circle class="outer-frame" cx="600" cy="600" r="584" fill="none" stroke="var(--frame-tan)" stroke-width="10"/>
      <circle class="centre-panel" cx="600" cy="600" r="394" fill="var(--label-white)" stroke="var(--frame-tan)" stroke-width="8"/>
    </svg>

    <p class="label-text company-name">Henrietta's<br>Little Oven Company</p>
    <h1 class="label-text flavour">Chocolate Chip</h1>
    <p class="label-text product-details">All Natural<br>New Wt. 8.0oz</p>
  </main>
</body>
</html>
```